Road Construction Company needs business cards

We would like a new business card designed for our business.

We're a road construction company based in Qld, Australia.

Can the business card please have the following information on it.

Name: Brent Malvoy
Position: General Manager
Phone: 0471 592 304
Email: Brent.malvoy@quendix.com.au
Address: 87 Harrowgate Ave, Pindarra, QLD, 4000
Website: www.quendix.com.au

Visually we'd like the card to be professional and simple.

Attached is our logo.

Our website is www.quendix.com.au

Target Market(s)

Men aged 25-60

Contact Information for Business Card

As listed in project description

Font styles to use
Serif

Requirements
Must have
• Large logo on back of card

```html
<!DOCTYPE html>
<html lang="en">
<head>
<meta charset="utf-8">
<title>Quendix Business Card</title>
<link rel="stylesheet" href="https://fonts.googleapis.com/css2?family=Barlow+Semi+Condensed:wght@500;600;700&family=Montserrat:wght@300;400&display=swap">
<style>
  :root {
    --page-bg: #dadada;
    --card-white: #ffffff;
    --brand-blue: #1155a3;
    --accent-blue: #2ea6d8;
    --asphalt-light: #dddee3;
    --asphalt-mid: #d2d3d9;
    --shadow: rgba(0,0,0,0.35);
  }
  * { box-sizing: border-box; margin: 0; padding: 0; }
  html, body { width: 1200px; height: 1200px; overflow: hidden; background: var(--page-bg); }
  .stage { position: relative; width: 1200px; height: 1200px; }

  .card {
    position: absolute;
    left: 304px;
    width: 604px;
    height: 345px;
    overflow: hidden;
    box-shadow: 1px 2px 4px var(--shadow);
  }
  .card--front { top: 202px; background: var(--card-white); }
  .card--back { top: 652px; }

  .card__waves { position: absolute; inset: 0; width: 100%; height: 100%; }

  .person { position: absolute; left: 39px; top: 32px; font-family: "Barlow Semi Condensed", sans-serif; }
  .person__name { font-size: 32px; font-weight: 600; color: var(--brand-blue); line-height: 1; letter-spacing: 0.2px; }
  .person__title { font-size: 15px; font-weight: 500; color: var(--accent-blue); letter-spacing: 0.9px; line-height: 1; margin-top: 2px; }

  .brand-name {
    font-family: "Barlow Semi Condensed", sans-serif;
    font-weight: 700;
    color: var(--brand-blue);
    line-height: 1;
  }
  .brand-name--front { position: absolute; right: 26px; top: 36px; font-size: 40px; letter-spacing: 7px; margin-right: -7px; }

  .contact-list { position: absolute; left: 39px; top: 174px; list-style: none; }
  .contact-list__item { display: flex; align-items: center; height: 26px; margin-bottom: 12.5px; }
  .contact-list__icon {
    width: 26px; height: 26px; border-radius: 6px; background: var(--card-white);
    display: flex; align-items: center; justify-content: center; margin-right: 8px;
  }
  .contact-list__icon svg { width: 18px; height: 18px; }
  .contact-list__text { font-family: "Montserrat", sans-serif; font-weight: 300; font-size: 14.5px; color: var(--card-white); }

  .card__photo {
    position: absolute; inset: 0;
    background: linear-gradient(180deg, var(--asphalt-light), var(--asphalt-mid));
  }
  .brand-name--back {
    position: absolute; left: 0; right: 0; top: 150px; text-align: center;
    font-size: 76px; letter-spacing: 20px; text-indent: 20px;
  }
  .back-web {
    position: absolute; left: 0; right: 0; top: 300px; text-align: center;
    font-family: "Montserrat", sans-serif; font-weight: 400; font-size: 14px;
    letter-spacing: 4px; color: var(--brand-blue);
  }
</style>
</head>
<body>
<main class="stage">
  <section class="card card--front">
    <svg class="card__waves" viewBox="0 0 971 555" preserveAspectRatio="none" aria-hidden="true">
      <path fill="var(--brand-blue)" d="M0 226 C60 185 140 172 240 180 C420 195 560 290 720 330 C830 355 910 335 971 292 L971 555 L0 555 Z"/>
      <path fill="var(--accent-blue)" d="M0 254 C60 220 140 206 240 210 C420 222 560 320 720 360 C830 385 910 368 971 320 L971 350 C910 395 830 410 720 390 C560 352 420 258 240 242 C140 236 60 250 0 286 Z"/>
    </svg>

    <div class="person">
      <h1 class="person__name">BRENT MALVOY</h1>
      <p class="person__title">GENERAL MANAGER</p>
    </div>

    <div class="brand-name brand-name--front">QUENDIX</div>

    <ul class="contact-list">
      <li class="contact-list__item">
        <span class="contact-list__icon"><svg viewBox="0 0 18 18"><rect x="5" y="1.5" width="8" height="15" rx="1.5" fill="none" stroke="var(--brand-blue)" stroke-width="1.6"/><circle cx="9" cy="14" r="0.9" fill="var(--brand-blue)"/></svg></span>
        <span class="contact-list__text">0471 592 304</span>
      </li>
      <li class="contact-list__item">
        <span class="contact-list__icon"><svg viewBox="0 0 18 18"><rect x="2" y="4" width="14" height="10" fill="none" stroke="var(--brand-blue)" stroke-width="1.4"/><path d="M2 4 L9 10 L16 4 M2 14 L7 8.5 M16 14 L11 8.5" fill="none" stroke="var(--brand-blue)" stroke-width="1.2"/></svg></span>
        <span class="contact-list__text">Brent.malvoy@quendix.com.au</span>
      </li>
      <li class="contact-list__item">
        <span class="contact-list__icon"><svg viewBox="0 0 18 18"><g fill="none" stroke="var(--brand-blue)" stroke-width="1.1"><circle cx="9" cy="9" r="7"/><ellipse cx="9" cy="9" rx="3" ry="7"/><path d="M2 9 H16 M3 5.5 H15 M3 12.5 H15"/></g></svg></span>
        <span class="contact-list__text">www.quendix.com.au</span>
      </li>
      <li class="contact-list__item">
        <span class="contact-list__icon"><svg viewBox="0 0 18 18"><path d="M9 15 C6 11 4.5 8.5 4.5 6.5 A4.5 4.5 0 0 1 13.5 6.5 C13.5 8.5 12 11 9 15 Z" fill="none" stroke="var(--brand-blue)" stroke-width="1.6"/><circle cx="9" cy="6.5" r="1.6" fill="var(--brand-blue)"/><ellipse cx="9" cy="16" rx="2.5" ry="0.8" fill="var(--brand-blue)"/></svg></span>
        <span class="contact-list__text">87 Harrowgate Ave, Pindarra, QLD, 4000</span>
      </li>
    </ul>
  </section>

  <section class="card card--back">
    <div class="card__photo" role="img" aria-label="Faded photograph of an asphalt road with centre line markings"></div>
    <div class="brand-name brand-name--back">QUENDIX</div>
    <p class="back-web">www.quendix.com.au</p>
  </section>
</main>
</body>
</html>
```